Real Estate Managemene Company Needs Business Card Design

We have a logo design and just need business cards made now for our business. Please use PDF logo # 3.

Card with Information to be attached shortly.

The card is used for a real estate management company. We will need to add four other employees and their cards.

Industry/Entity Type

Real Estate

Contact Information for Business Card

Tariq Hamdan
President
3187 Thornwick Avenue
Suite C
Glendale Heights, IL 60152
Phone 630.417.2286
Fax 630.417.2287
Cell 630.473.8062
vantorp@mailbreeze.net

Once design is approved we will have four other employees
Omar Hamdan
Operations Manager

Nadia Hamdan
Administrative Manager

Faz Hamdan
Principal

We would need to take out the cell # 630.473.8062 out for the remaining three cards.

Requirements
Must have
• Please use logo attached

```html
<!DOCTYPE html>
<html lang="en">
<head>
<meta charset="utf-8">
<title>Halvern Property Management Group – Business Card</title>
<link href="https://fonts.googleapis.com/css2?family=Open+Sans:wght@400;600&family=Tenor+Sans&display=swap" rel="stylesheet">
<style>
  :root {
    --backdrop: #e9e7e4;
    --card: #ffffff;
    --ink: #1c1c1c;
    --brand-blue: #1d4f8c;
    --divider: #8a8a8a;
  }
  * { box-sizing: border-box; margin: 0; padding: 0; }
  html, body {
    width: 1200px; height: 1000px; overflow: hidden;
    background: var(--backdrop);
  }
  .canvas { position: relative; width: 1200px; height: 1000px; }
  .card {
    position: absolute; left: 265px; width: 666px; height: 397px;
    background: var(--card);
    box-shadow: 0 2px 6px rgba(0,0,0,0.18);
  }
  .card--front { top: 73px; }
  .card--second { top: 532px; }

  .brand-mark {
    position: absolute; left: 293px; top: 42px; width: 80px; height: 80px;
    background: var(--brand-blue);
  }
  .brand-name {
    position: absolute; left: 0; right: 0; top: 150px;
    text-align: center;
    font-family: "Open Sans", sans-serif; font-weight: 600;
    font-size: 27px; line-height: 34px;
    color: var(--ink);
  }

  .holder {
    position: absolute; right: 353px; top: 262px; text-align: right;
  }
  .holder__name {
    font-family: "Tenor Sans", sans-serif; font-size: 21px;
    color: var(--brand-blue); letter-spacing: 0.5px; line-height: 24px;
  }
  .holder__title {
    font-family: "Open Sans", sans-serif; font-size: 15px;
    color: var(--ink); line-height: 22px;
  }

  .divider {
    position: absolute; left: 331px; top: 244px; width: 1px; height: 84px;
    background: linear-gradient(to bottom, transparent, var(--divider) 20%, var(--divider) 80%, transparent);
  }

  .contact-list {
    position: absolute; left: 354px; top: 242px; list-style: none;
    font-family: "Open Sans", sans-serif; font-size: 14.5px; color: var(--ink);
  }
  .contact-list li {
    display: flex; align-items: center; height: 22px; gap: 8px;
  }
  .contact-list svg { width: 13px; height: 13px; fill: var(--brand-blue); flex: none; }

  .address {
    position: absolute; left: 0; right: 0; top: 348px; text-align: center;
    font-family: "Open Sans", sans-serif; font-size: 16px; color: var(--ink);
  }
</style>
</head>
<body>
<svg width="0" height="0" style="position:absolute">
  <defs>
    <symbol id="icon-mobile" viewBox="0 0 12 16"><path d="M3 0h6a2 2 0 0 1 2 2v12a2 2 0 0 1-2 2H3a2 2 0 0 1-2-2V2a2 2 0 0 1 2-2zm0 2v10h6V2zm3 11a1 1 0 1 0 0 2 1 1 0 0 0 0-2z"/></symbol>
    <symbol id="icon-phone" viewBox="0 0 16 14"><path d="M1 4c0-2 3-3 7-3s7 1 7 3v1h-4V3.5H5V5H1zM4 6h8l2 6H2zm4 1.5a2 2 0 1 0 0 4 2 2 0 0 0 0-4z"/></symbol>
    <symbol id="icon-fax" viewBox="0 0 16 14"><path d="M4 0h8v4H4zM1 5h14v6h-3v3H4v-3H1zm4 4v4h6V9z"/></symbol>
    <symbol id="icon-mail" viewBox="0 0 16 12"><path d="M0 0h16v12H0zm1.5 1.5L8 6.5l6.5-5zm0 1.6V10.5h13V3.1L8 8.2z"/></symbol>
  </defs>
</svg>

<div class="canvas">
  <section class="card card--front">
    <div class="brand-mark"></div>
    <div class="brand-name">Halvern<br>Property Management Group</div>
    <div class="holder">
      <p class="holder__name">TARIQ HAMDAN</p>
      <p class="holder__title">President</p>
    </div>
    <div class="divider"></div>
    <ul class="contact-list">
      <li><svg><use href="#icon-mobile"/></svg>630.473.8062</li>
      <li><svg><use href="#icon-phone"/></svg>630.417.2286</li>
      <li><svg><use href="#icon-fax"/></svg>630.417.2287</li>
      <li><svg><use href="#icon-mail"/></svg>www.vantorp@mailbreeze.net</li>
    </ul>
    <p class="address">3187 Thornwick Avenue, Suite C, Glendale Heights, IL 60152</p>
  </section>

  <section class="card card--second">
    <div class="brand-mark"></div>
    <div class="brand-name">Halvern<br>Property Management Group</div>
    <div class="holder">
      <p class="holder__name">TARIQ HAMDAN</p>
      <p class="holder__title">President</p>
    </div>
    <div class="divider"></div>
    <ul class="contact-list">
      <li><svg><use href="#icon-mobile"/></svg>630.473.8062</li>
      <li><svg><use href="#icon-phone"/></svg>630.417.2286</li>
      <li><svg><use href="#icon-fax"/></svg>630.417.2287</li>
      <li><svg><use href="#icon-mail"/></svg>www.vantorp@mailbreeze.net</li>
    </ul>
    <p class="address">3187 Thornwick Avenue, Suite C, Glendale Heights, IL 60152</p>
  </section>
</div>
</body>
</html>
```